" Somos a Casa Lumiar, uma empresa que atua no vareja em Fortaleza - CE e já estamos a mais de 20 anos no ramo. Nós vendemos produtos gastronômicos de marcas como: tavares, gelmar, brixley... para restaurantes, padaria, confeitarias, escolas de culinárias, cozinhas industriais em geral. Oferecemos atendimento atualmente em loja física principalmente presencial, e por ligação, além de termos um site(não vendemos por ele). A ideia é que dentro de 2 meses trabalhemos apenas com atendimento externo, por ligação e por ecommerce, ou seja, de portas fechadas. O objetivo é diminuir a passividade do setor comercial e aumentar a personalização do nosso atendimento para os maiores clientes do mercado. Somos umas das maiores empresas do ramo em Fortaleza e provavelmente a melhor em questão de atendimento ao cliente. Nossa identidade é: * Visão: * A Casa Lumiar como a maior fornecedora de equipamentos de ponta para os principais negócios gastronômicos do Ceará. E como principal parceira no ceará dos pequenos negócios da área gastronômica. * Missão: * Nós ajudamos empreendedores do setor gastronômico a equiparem seus negócios com soluções em automação e produção. * Valores: * Excelência: Fazer tudo da melhor maneira possível. * Simplicidade. * Foco no próximo: Satisfazer a *necessidade* do outro, se preciso antes da própria necessidade. * Integridade: Fazer tudo de forma correta e as claras, com transparência e honestidade. * Inovação: Buscar pelo novo e por fazer diferente e melhor aquilo que já se faz. * Sucesso: Desenvolver a plenitude e a paz interior e impactar a exterior com atitudes. * Responsabilidade: Responder pelas próprias atitudes, tomar para si seus deveres e lidar com suas consequências. "

```html
<!DOCTYPE html>
<html lang="pt-BR">
<head>
<meta charset="utf-8">
<title>Casa Lumiar – Bares e Restaurantes</title>
<link rel="stylesheet" href="https://fonts.googleapis.com/css2?family=Arimo:wght@400;700&display=swap">
<style>
  :root {
    --green-dark: #0b4a1c;
    --green: #127a2e;
    --green-light: #2a9a3f;
    --gold: #c9a34a;
    --gold-light: #ecd089;
    --white: #ffffff;
    --page: #ffffff;
    --text-dark: #1f3a24;
  }
  * { margin: 0; padding: 0; box-sizing: border-box; }
  html, body { width: 1200px; height: 1200px; overflow: hidden; background: var(--page); }
  body { font-family: "Arimo", Arial, sans-serif; }
  .flyer {
    position: absolute; left: 144px; top: 0; width: 912px; height: 1200px;
    background: var(--white); overflow: hidden;
  }
  .header-wave { position: absolute; left: 0; top: 0; width: 912px; height: 90px; }
  .photo-chef {
    position: absolute; left: 360px; top: 40px; width: 552px; height: 700px;
    background: linear-gradient(160deg, #f4f4f2 0%, #e6e6e2 45%, #c9cdc5 80%, #8fae5a 100%);
  }
  .photo-oven {
    position: absolute; left: 36px; top: 380px; width: 360px; height: 245px;
    background: linear-gradient(180deg, #5b5b5b 0%, #2c2c2c 55%, #1b1b1b 100%);
  }
  .brand {
    position: absolute; left: 0; top: 46px; width: 330px;
    display: flex; flex-direction: column; align-items: center;
  }
  .brand-mark {
    width: 92px; height: 92px; border-radius: 50%;
    border: 5px solid var(--gold); background: var(--white);
  }
  .brand-name {
    margin-top: 14px; font-size: 34px; font-weight: 700;
    color: var(--text-dark); letter-spacing: 1px;
  }
  .brand-tagline {
    margin-top: 4px; font-size: 10px; color: var(--text-dark);
    text-transform: uppercase; letter-spacing: .5px;
  }
  .segment-band { position: absolute; left: 0; top: 610px; width: 912px; height: 140px; }
  .segment-label {
    position: absolute; left: 0; top: 620px; width: 492px; height: 66px;
    display: flex; align-items: center; padding-left: 30px;
    background: linear-gradient(90deg, var(--green-dark), var(--green));
    color: var(--white); font-size: 38px; font-weight: 700;
  }
  .offer-panel {
    position: absolute; left: 0; top: 744px; width: 912px; height: 426px;
    background: radial-gradient(ellipse at 80% 30%, var(--green-light) 0%, var(--green) 40%, var(--green-dark) 100%);
    border-top: 6px solid var(--gold);
  }
  .offer-lines { position: absolute; left: 0; top: 0; width: 912px; height: 426px; }
  .offer-title {
    position: absolute; left: 42px; top: 28px;
    color: var(--white); font-size: 58px; font-weight: 700; line-height: 1.12;
  }
  .offer-cta {
    position: absolute; left: 42px; top: 240px;
    color: var(--white); font-size: 30px; font-weight: 700;
  }
  .footer-strip {
    position: absolute; left: 0; bottom: 0; width: 912px; height: 30px;
    background: linear-gradient(90deg, var(--gold), var(--gold-light), var(--gold));
  }
</style>
</head>
<body>
  <main class="flyer">
    <svg class="header-wave" viewBox="0 0 912 90" preserveAspectRatio="none">
      <path d="M0 0 H912 V12 C700 30 420 60 0 70 Z" fill="var(--gold)"/>
      <path d="M0 0 H912 V6 C700 22 420 48 0 58 Z" fill="var(--gold-light)"/>
    </svg>

    <div class="photo-chef" role="img" aria-label="Foto de cozinheira de dólmã branco cortando legumes em tábua de madeira"></div>
    <div class="photo-oven" role="img" aria-label="Foto de fogão industrial de quatro bocas com forno"></div>

    <div class="brand">
      <span class="brand-mark"></span>
      <span class="brand-name">Casa Lumiar</span>
      <span class="brand-tagline">a parceira certa para o seu negócio</span>
    </div>

    <svg class="segment-band" viewBox="0 0 912 140" preserveAspectRatio="none">
      <path d="M0 76 H500 C640 76 760 110 912 134 V140 H0 Z" fill="var(--green)"/>
      <path d="M0 82 H500 C640 82 760 114 912 138" stroke="var(--gold)" stroke-width="3" fill="none"/>
    </svg>
    <div class="segment-label">Bares e Restarantes</div>

    <section class="offer-panel">
      <svg class="offer-lines" viewBox="0 0 912 426" preserveAspectRatio="none">
        <path d="M0 215 H520 C640 215 760 200 912 170" stroke="var(--gold)" stroke-width="3" fill="none"/>
        <path d="M0 300 H600 C720 300 820 320 912 340" stroke="var(--gold-light)" stroke-width="2" fill="none" opacity=".6"/>
      </svg>
      <h1 class="offer-title">Trabalhamos com os<br>melhores FORNECEDORES<br>do mercado</h1>
      <p class="offer-cta">Conheca as marcas</p>
    </section>

    <div class="footer-strip"></div>
  </main>
</body>
</html>
```